IT Company based on Biology Business Needs a Business Card Design

We need a business card design for a new company called 'Lumen CELL'. We develop the machine learning solutions especially focused on deep learning algorithms for biology industry. Our initial product is a vision detection on biological images to help doctors diagnose the symptoms. We would like to see designs that use the color green.

Industry/Entity Type

Business

```html
<!DOCTYPE html>
<html lang="en">
<head>
<meta charset="utf-8">
<title>Lumen CELL – Business Card</title>
<link href="https://fonts.googleapis.com/css2?family=Open+Sans:wght@400;600&display=swap" rel="stylesheet">
<style>
  :root {
    --page-bg: #5a5a5a;
    --card-dark: #1c1d1c;
    --card-dark-glow: #353735;
    --card-light: #ffffff;
    --green-bright: #6cc04a;
    --green-mid: #3fa535;
    --green-deep: #1e8a3a;
    --text-dark: #1f2a2a;
    --text-muted: #3a4444;
    --tint: #eef3ee;
  }
  * { box-sizing: border-box; margin: 0; padding: 0; }
  html, body { width: 1200px; height: 834px; overflow: hidden; }
  body {
    background: var(--page-bg);
    font-family: "Open Sans", Arial, sans-serif;
    display: flex; flex-direction: column; align-items: center; justify-content: center;
    gap: 40px;
  }
  .card { width: 560px; height: 320px; position: relative; overflow: hidden; border-radius: 2px; box-shadow: 0 8px 24px rgba(0,0,0,.35); }

  /* back side */
  .card--back { background: var(--card-dark); }
  .card--back .pattern {
    position: absolute; inset: 0;
    background: radial-gradient(ellipse at 50% 45%, var(--card-dark-glow) 0%, var(--card-dark) 70%);
  }
  .brand { position: absolute; display: flex; align-items: center; gap: 12px; color: var(--green-bright); font-weight: 600; letter-spacing: -1px; }
  .brand__dot { width: 22px; height: 22px; border-radius: 50%; background: var(--green-bright); }
  .card--back .brand { left: 50%; top: 50%; transform: translate(-50%, -50%); font-size: 46px; }

  /* front side */
  .card--front { background: var(--card-light); }
  .card--front .side-deco {
    position: absolute; right: 0; top: 0; width: 130px; height: 210px;
    background: linear-gradient(200deg, var(--tint) 0%, rgba(238,243,238,0) 85%);
  }
  .card--front .swoosh { position: absolute; left: 0; bottom: 0; width: 560px; height: 140px; }
  .card--front .brand { left: 48px; top: 178px; font-size: 38px; }
  .card--front .brand__dot { width: 18px; height: 18px; }

  .contact { position: absolute; left: 300px; top: 40px; color: var(--text-dark); }
  .contact__name { font-size: 17px; font-weight: 600; }
  .contact__role { font-size: 12px; color: var(--green-bright); margin-bottom: 14px; }
  .contact__address { font-size: 11.5px; color: var(--text-muted); margin-bottom: 16px; }
  .contact__list { list-style: none; font-size: 11.5px; color: var(--text-muted); }
  .contact__list li { display: flex; align-items: center; gap: 10px; line-height: 20px; }
  .contact__list svg { width: 13px; height: 13px; stroke: var(--green-mid); fill: none; stroke-width: 1.4; }
</style>
</head>
<body>

<section class="card card--back" aria-label="Card back">
  <div class="pattern" role="img" aria-label="Dark background with faint repeating green molecule pattern"></div>
  <div class="brand"><span class="brand__dot"></span>Lumen CELL</div>
</section>

<section class="card card--front" aria-label="Card front">
  <div class="side-deco" role="img" aria-label="Faint pale green molecule decoration"></div>

  <div class="contact">
    <p class="contact__name">Mara Ellis</p>
    <p class="contact__role">President</p>
    <p class="contact__address">17 Harlow Row, York, UK, YO1 4RT</p>
    <ul class="contact__list">
      <li><svg viewBox="0 0 14 14"><rect x="4" y="1" width="6" height="12" rx="1"/></svg>+44 (0) 7700 310 482</li>
      <li><svg viewBox="0 0 14 14"><path d="M2 6 Q7 1 12 6 L10 7 L9 5 H5 L4 7 Z"/><rect x="3" y="8" width="8" height="5" rx="1"/></svg>+44 (0) 7700 310 495</li>
      <li><svg viewBox="0 0 14 14"><rect x="1" y="3" width="12" height="8"/><path d="M1 3 L7 8 L13 3"/></svg>mara@lumencell.life</li>
      <li><svg viewBox="0 0 14 14"><circle cx="7" cy="7" r="6"/><path d="M1 7 H13 M7 1 Q3 7 7 13 M7 1 Q11 7 7 13"/></svg>www.lumencell.life</li>
    </ul>
  </div>

  <div class="brand"><span class="brand__dot"></span>Lumen CELL</div>

  <svg class="swoosh" viewBox="0 0 560 140" preserveAspectRatio="none" aria-hidden="true">
    <path d="M0 140 L0 108 Q300 110 560 20 L560 140 Z" fill="var(--green-deep)"/>
    <path d="M0 104 Q300 104 560 12 L560 22 Q300 112 0 108 Z" fill="var(--green-bright)"/>
  </svg>
</section>

</body>
</html>
```